Vor Plimm business card

Create a new business card for Vor Plimm. Black colour base front and back (the sides can be blue if that works) You can modify the blue colour to best suit the design. I am after a card that looks technical, modern and strong. one side with the Vor Plimm and the other company details. The attached file has the details needed for the card. Flipside is the parent company name and needed but in a smaller size

Target Market(s)

Businesses (suppliers and customers)

Industry/Entity Type

Business

Contact Information for Business Card

Black colour base front and back

Font styles to use
Other font styles liked:
• attached

Requirements
Must have
• Logo's as attached

```html
<!DOCTYPE html>
<html lang="en">
<head>
<meta charset="utf-8">
<title>Vor Plimm business card</title>
<link rel="stylesheet" href="https://fonts.googleapis.com/css2?family=Open+Sans:wght@400;600;700&display=swap">
<style>
  :root {
    --bg: #2b2f34;
    --card-black: #1f1c1d;
    --card-white: #ffffff;
    --accent-blue: #1c9bdc;
    --text-light: #e9e9ea;
    --text-muted: #b4b4b6;
    --text-dark: #3a3a3c;
    --emboss: #4a4a4d;
  }
  * { margin: 0; padding: 0; box-sizing: border-box; }
  html, body { width: 1200px; height: 900px; overflow: hidden; }
  body {
    background: var(--bg);
    display: flex;
    flex-direction: column;
    align-items: center;
    justify-content: center;
    gap: 40px;
    font-family: "Open Sans", sans-serif;
  }
  .card {
    position: relative;
    width: 700px;
    height: 400px;
    border-radius: 22px;
    overflow: hidden;
    background: var(--card-black);
  }
  .card__wave { position: absolute; inset: 0; }

  .brand__name {
    font-family: "Open Sans", sans-serif;
    font-weight: 700;
    letter-spacing: 3px;
    line-height: 1;
    white-space: nowrap;
  }
  .slogan {
    font-family: "Open Sans", sans-serif;
    font-weight: 600;
    letter-spacing: 5px;
    text-transform: uppercase;
    white-space: nowrap;
  }

  .front .brand { position: absolute; left: 44px; top: 54px; }
  .front .brand__name { font-size: 50px; color: var(--text-light); }
  .front .slogan { position: absolute; left: 46px; top: 116px; font-size: 14px; color: var(--accent-blue); }

  .person { position: absolute; right: 36px; top: 150px; text-align: right; }
  .person__name {
    font-weight: 600;
    font-size: 26px;
    color: var(--accent-blue);
    letter-spacing: 1px;
  }
  .person__role { font-size: 15px; color: var(--text-dark); margin-top: 2px; }

  .contact { position: absolute; left: 44px; top: 196px; list-style: none; }
  .contact li {
    display: flex; align-items: center; gap: 10px;
    font-size: 14px; color: var(--text-muted); line-height: 24px;
  }
  .contact svg { width: 12px; height: 12px; fill: var(--accent-blue); }

  .divider {
    position: absolute; left: 44px; top: 290px;
    width: 400px; height: 2px; background: var(--accent-blue);
  }
  .address {
    position: absolute; left: 44px; top: 306px;
    font-size: 15px; line-height: 22px; color: var(--text-muted);
  }

  .back .lockup {
    position: absolute; inset: 0;
    display: flex; flex-direction: column; align-items: center; justify-content: center;
    gap: 14px;
  }
  .back .brand__name { font-size: 68px; color: var(--emboss); }
  .back .slogan { font-size: 18px; color: var(--emboss); letter-spacing: 8px; }
</style>
</head>
<body>
  <section class="card front">
    <svg class="card__wave" viewBox="0 0 700 400" aria-hidden="true">
      <path d="M430,0 C380,130 560,230 500,400 L700,400 L700,0 Z" fill="var(--accent-blue)"/>
      <path d="M462,0 C412,130 592,230 532,400 L700,400 L700,0 Z" fill="var(--card-black)"/>
      <path d="M470,0 C420,130 600,230 540,400 L700,400 L700,0 Z" fill="var(--card-white)"/>
    </svg>
    <div class="brand">
      <div class="brand__name">VOR PLIMM</div>
    </div>
    <p class="slogan">Smart Gear For Pets</p>
    <div class="person">
      <div class="person__name">LENA HART</div>
      <div class="person__role">Managing Director</div>
    </div>
    <ul class="contact">
      <li><svg viewBox="0 0 12 12"><path d="M2.5 1 L4.5 1 L5.3 3.5 L4 4.4 C4.7 6 6 7.3 7.6 8 L8.5 6.7 L11 7.5 L11 9.5 C11 10.3 10.3 11 9.5 11 C5 11 1 7 1 2.5 C1 1.7 1.7 1 2.5 1 Z"/></svg>+61 400 555 019</li>
      <li><svg viewBox="0 0 12 12"><path d="M1 2.5 H11 V9.5 H1 Z M1.5 3 L6 6.5 L10.5 3" fill="none" stroke="var(--accent-blue)" stroke-width="1.2"/></svg>lena@harbourline.com</li>
      <li><svg viewBox="0 0 12 12"><circle cx="6" cy="6" r="4.8" fill="none" stroke="var(--accent-blue)" stroke-width="1.2"/><path d="M1.2 6 H10.8 M6 1.2 C3.8 4 3.8 8 6 10.8 M6 1.2 C8.2 4 8.2 8 6 10.8" fill="none" stroke="var(--accent-blue)" stroke-width="1"/></svg>www.harbourline.com</li>
    </ul>
    <div class="divider"></div>
    <p class="address">PO Box 120 Norwood,<br>S.A. 5067, Australia</p>
  </section>

  <section class="card back">
    <div class="lockup">
      <div class="brand__name">VOR PLIMM</div>
      <p class="slogan">Smart Gear For Pets</p>
    </div>
  </section>
</body>
</html>
```